Web Design Project

We are an IT System Integrator. We provide Norvik 500 ERP System, CRM etc. We also provide hardware, networking servicing. Please look at www.brinquot.com.sg. They provide the same service as us. We like to redesign our web site. I will attached the color that I prefer for reference.

Our website is www.ravdu.com.sg.  It has been created about 14 years ago.  We are trying to revamp it with a new look and information.   The new website must be informative, fast.    I have attached an attachment which show the color that I prefer(brownish golden).   

Our competitor (www.brinquot.com) is carrying the same trade as us.  They have all the informations In their website that we will like to have.  Therefore I recommend you to take a look at my competitor website and have a better   
understanding on the kind of information I would like to have for my new website.

This project is guarantee to the person with the best design.  We can have it guarantee.

Target Market(s)

Corporate and companies

Industry/Entity Type

Hardware

```html
<!DOCTYPE html>
<html lang="en">
<head>
<meta charset="utf-8">
<title>Quantrel Information Systems</title>
<link href="https://fonts.googleapis.com/css2?family=Arimo:wght@400;700&family=PT+Sans+Narrow:wght@700&family=Michroma&display=swap" rel="stylesheet">
<style>
:root{
  --gold:#b87a2c;
  --gold-light:#d49a48;
  --ink:#222;
  --text:#333;
  --muted:#666;
  --line:#ccc;
  --dark:#2a2a2a;
  --footer:#3b3b3b;
  --white:#fff;
}
*{margin:0;padding:0;box-sizing:border-box}
html,body{width:1190px;height:1200px;overflow:hidden}
body{position:relative;font-family:Arimo,Arial,sans-serif;color:var(--text);
  background:linear-gradient(#f3f3f3 0,#e9e9e9 300px,#c9c9cb 382px,#f4f4f4 383px,#fff 700px,#fff 1034px)}
.abs{position:absolute}
.top-strip{left:0;top:0;width:1190px;height:7px;background:var(--gold)}
.util-nav{left:655px;top:0;width:300px;height:24px;background:var(--gold);border-radius:0 0 8px 8px;
  color:#fff;font-size:10px;display:flex;justify-content:center;align-items:center;gap:6px;white-space:nowrap}
.brand{left:340px;top:42px;display:flex;align-items:center;gap:14px}
.brand-mark{width:18px;height:18px;background:var(--gold);border-radius:50%}
.brand-name{color:var(--gold);font-weight:700;font-size:10.5px;line-height:21px;white-space:nowrap}
.phones{right:244px;top:80px;text-align:right;font-size:15px;color:#444;line-height:26px;white-space:nowrap}
.phones b{color:var(--gold);font-size:19px;font-weight:700;margin-left:4px}
.phones svg{vertical-align:-3px;margin-right:6px}
.main-nav{left:226px;top:136px;width:744px;height:44px;background:#111;border-radius:4px 4px 0 0;
  border-bottom:4px solid var(--gold);display:flex;align-items:stretch}
.main-nav a{color:#fff;font-weight:700;font-size:11.5px;text-decoration:none;padding:0 15px;white-space:nowrap;
  display:flex;align-items:center;border-right:1px solid #333;flex-shrink:0}
.main-nav a.active{background:linear-gradient(#c88a3a,#a86a20);border:0}
.search{margin:6px 6px 6px auto;width:132px;flex-shrink:0;background:#fff;border-radius:2px;display:flex;white-space:nowrap;
  align-items:center;justify-content:space-between;padding:0 6px;font-size:10px;color:#555}
.hero{left:226px;top:180px;width:742px;height:262px;background:#fff;overflow:hidden}
.hero-art{left:40px;top:8px;width:240px;height:250px;border-radius:50%;
  background:radial-gradient(circle at 50% 40%,#e3c24a 0,#5aa4d6 30%,#8cbf3a 45%,#e6e6e6 65%,#fff 72%)}
.hero-panel{left:0;top:0}
.hero-title{left:437px;top:36px;font-family:Michroma,sans-serif;color:#fff;font-size:17px;letter-spacing:1.5px;line-height:27px;white-space:nowrap}
.hero-copy{left:434px;top:118px;width:250px;font-family:"PT Sans Narrow",sans-serif;color:#fff;font-size:14.5px;line-height:21px}
.hero-btn{left:434px;top:210px;width:150px;height:28px;border-radius:14px;background:linear-gradient(#d09a4e,#a66a22);
  color:#fff;font-weight:700;font-size:13.5px;display:flex;align-items:center;justify-content:center}
.arrow{width:22px;height:32px;background:#fff;box-shadow:0 1px 3px rgba(0,0,0,.3);display:flex;align-items:center;justify-content:center}
.welcome{left:252px;top:474px;width:696px;height:44px;border-bottom:1px dotted #aaa;display:flex;align-items:center;gap:12px}
.welcome-mark{width:16px;height:16px;background:var(--gold);border-radius:50%}
.welcome h1{font-size:18px;font-weight:400;color:var(--gold);white-space:nowrap}
.welcome h1 strong{color:var(--ink);font-weight:700}
.intro{left:252px;top:532px;width:700px;font-size:8.6px;line-height:14.3px;color:#222}
.card{top:650px;width:218px;height:232px;background:linear-gradient(#fff,#ececec);border:1px solid #bbb;
  box-shadow:0 0 0 3px #f4f4f4 inset}
.card-photo{left:10px;top:9px;width:198px;height:90px}
.card h2{position:absolute;left:14px;top:112px;font-size:14px;font-weight:400;color:#222;white-space:nowrap}
.card h2 span{color:var(--gold)}
.card ul{position:absolute;left:14px;top:142px;list-style:none;font-size:9.3px;line-height:15px;color:#333;white-space:nowrap}
.card li::before{content:"»";margin-right:4px;font-weight:700}
.card .more{position:absolute;right:12px;bottom:12px;font-size:9.3px;color:#222}
.card .more span{color:var(--gold)}
.contact{left:726px;top:650px;width:218px;height:232px;background:linear-gradient(#fff,#ececec);border:1px solid #bbb;padding:10px 12px}
.contact h2{text-align:center;font-size:15px;font-weight:700;color:#222;margin-bottom:6px}
.contact h2 span{color:var(--gold)}
.field{height:19px;border:1px solid #ccc;background:#fff;margin-bottom:3px;font-size:8.5px;color:#888;padding:4px 8px;
  box-shadow:0 0 0 2px #f2f2f2;display:flex;justify-content:space-between}
.field.tall{height:50px}
.actions{display:flex;gap:6px;margin-top:6px}
.btn{width:72px;height:20px;border:1px solid #ccc;background:#fff;display:flex;justify-content:space-between;align-items:center;
  padding-left:6px;font-size:10.5px;color:#222}
.btn.ghost{color:#999}
.btn i{width:22px;height:18px;background:var(--gold);display:flex;align-items:center;justify-content:center}
.partners{left:251px;top:922px;width:692px;height:78px;background:linear-gradient(#fff,#eee);border:1px solid #ccc;
  display:flex;align-items:center;justify-content:space-around;padding:0 26px;font-weight:700;font-size:17px;color:#222}
.partners span:nth-child(2n){color:#1d4f99}
.pager{top:950px;width:20px;height:20px;background:#9a9a9a;border-radius:2px;display:flex;align-items:center;justify-content:center}
.footer{left:0;top:1034px;width:1190px;height:138px;background:var(--footer)}
.footer h3{position:absolute;color:var(--gold-light);font-size:10.5px;font-weight:700;white-space:nowrap}
.links{position:absolute;list-style:none;font-size:8.8px;color:#ccc;white-space:nowrap}
.links li{width:80px;border-bottom:1px dotted #777;height:15px;line-height:14px;overflow:hidden}
.links.wide li{width:96px}
.links li::before{content:"»";margin:0 6px 0 4px;color:#999}
.vrule{position:absolute;top:30px;width:1px;height:90px;border-left:1px dotted #777}
.social{position:absolute;color:#ddd;font-weight:700;font-size:11px;display:flex;align-items:center;gap:8px;white-space:nowrap}
.social i{width:16px;height:16px;background:#3b6ea8;border-radius:2px}
.f-brand{position:absolute;left:776px;top:28px;display:flex;align-items:center;gap:8px}
.f-brand div{color:var(--gold);font-size:8px;font-weight:700;line-height:14px;white-space:nowrap}
.subscribe{position:absolute;left:780px;top:76px;color:#ccc;font-weight:700;font-size:13px;white-space:nowrap}
.sub-row{position:absolute;left:780px;top:98px;display:flex;gap:5px}
.sub-row div:first-child{width:104px;height:15px;background:#fff;border-radius:2px;font-size:8px;color:#999;padding:2px 5px}
.sub-row div:last-child{height:13px;background:var(--gold);border-radius:2px;font-size:7.5px;color:#fff;padding:1px 4px}
.copyright{left:0;top:1172px;width:1190px;height:28px;background:linear-gradient(#c08236,#a66c25);color:#fff;
  font-size:10px;display:flex;align-items:center;justify-content:center}
</style>
</head>
<body>
<div class="abs top-strip"></div>
<nav class="abs util-nav"><span>Home</span>|<span>Log Incident</span>|<span>Enquiry</span>|<span>Contact</span>|<span>Client Support</span></nav>

<div class="abs brand"><div class="brand-mark"></div><div class="brand-name">QUANTREL<br>INFORMATION<br>SYSTEMS PTE LTD</div></div>

<div class="abs phones">
  <div><svg width="14" height="14" viewBox="0 0 24 24"><path fill="#b87a2c" d="M6.6 10.8a15 15 0 0 0 6.6 6.6l2.2-2.2c.3-.3.7-.4 1-.2 1.1.4 2.3.6 3.6.6.6 0 1 .4 1 1V20c0 .6-.4 1-1 1A17 17 0 0 1 3 4c0-.6.4-1 1-1h3.5c.6 0 1 .4 1 1 0 1.3.2 2.5.6 3.6.1.3 0 .7-.2 1z"/></svg>Phone #:<b>(065) 6120-4478</b></div>
  <div>Toll Free Phone#:<b>018.330.5261</b></div>
</div>

<nav class="abs main-nav">
  <a class="active">COMPANY</a><a>PRODUCTS</a><a>LEDGRA</a><a>SERVICES</a><a>CLIENTELE</a><a>CAREERS</a><a>INFOBIN</a>
  <div class="search">Search here<svg width="16" height="16" viewBox="0 0 20 20"><circle cx="8" cy="8" r="5.5" fill="none" stroke="#b87a2c" stroke-width="2"/><path d="M12 12l6 6" stroke="#b87a2c" stroke-width="3"/></svg></div>
</nav>

<section class="abs hero">
  <div class="abs hero-art" role="img" aria-label="Illustration of four figures joining coloured puzzle pieces"></div>
  <svg class="abs hero-panel" width="742" height="262" viewBox="0 0 742 262">
    <defs><radialGradient id="panelShade" cx="0.5" cy="0.2" r="0.8"><stop offset="0" stop-color="#6a6a6a"/><stop offset="1" stop-color="#262626"/></radialGradient></defs>
    <path d="M500 262 C 280 190, 340 20, 470 0 L742 0 L742 262 Z" fill="#b87a2c"/>
    <path d="M512 262 C 300 190, 360 25, 490 0 L742 0 L742 262 Z" fill="#777"/>
    <path d="M524 262 C 320 190, 380 30, 510 0 L742 0 L742 262 Z" fill="url(#panelShade)"/>
  </svg>
  <div class="abs hero-title">QUANTREL<br>INFORMATION<br>SYSTEMS PTE LTD</div>
  <p class="abs hero-copy">For more than 20 years, LEDGRA has provided reliable software solutions optimized to take advantage of new technologies and meet the unique requirements of companies.</p>
  <div class="abs hero-btn">Click to Read More</div>
</section>
<div class="abs arrow" style="left:222px;top:287px"><svg width="10" height="14"><path d="M8 1L2 7l6 6" stroke="#111" stroke-width="2.5" fill="none"/></svg></div>
<div class="abs arrow" style="left:949px;top:287px"><svg width="10" height="14"><path d="M2 1l6 6-6 6" stroke="#111" stroke-width="2.5" fill="none"/></svg></div>

<div class="abs welcome"><div class="welcome-mark"></div><h1>Welcome to <strong>QUANTREL INFORMATION</strong> SYSTEMS</h1></div>
<p class="abs intro">Lorem ipsum dolor sit amet, consectetuer adipiscing elit, sed diam nonummy nibh euismod tincidunt ut laoreet dolore magna aliquam erat volutpat. Ut wisi enim ad minim veniam, quis nostrud exerci tation ullamcorper suscipit lobortis nisl ut aliquip ex ea commodo consequat. Duis autem vel eum iriure dolor in hendrerit in vulputate velit esse molestie consequat, vel illum dolore eu feugiat nulla facilisis at vero eros et accumsan et iusto odio dignissim qui blandit praesent luptatum zzril delenit augue duis dolore te feugait nulla Lorem ipsum dolor sit amet, consectetuer adipiscing elit, sed diam nonummy nibh euismod tincidunt ut laoreet dolore magna aliquam erat volutpat. Ut wisi enim ad minim veniam, quis nostrud exerci tation ullamcorper suscipit lobortis nisl ut aliquip ex ea commodo consequat. Duis autem vel eum iriure dolor in hendrerit in vulputate velit esse molestie consequat, vel illum dolore eu feugiat nulla facilisis at vero eros et accumsan et iusto odio dignissim qui blandit praesent luptatum zzril delenit augue duis dolore te feugait nullai.</p>

<article class="abs card" style="left:251px">
  <div class="abs card-photo" role="img" aria-label="Photo of a server room aisle" style="background:linear-gradient(90deg,#222,#777 50%,#222)"></div>
  <h2>Managed <span>IT Services</span></h2>
  <ul><li>Migrations &amp; Upgrades to the 9's</li><li>Report Development</li><li>Custom Applications Development</li><li>Technical and CNC</li></ul>
  <div class="more">Read <span>More</span></div>
</article>
<article class="abs card" style="left:487px">
  <div class="abs card-photo" role="img" aria-label="Photo of a blue globe beside server racks" style="background:linear-gradient(90deg,#2a7fd6,#1a4f9a 35%,#333 45%,#888 75%,#eee)"></div>
  <h2>IT Consulting <span>Services</span></h2>
  <ul><li>Orvata Software and Technology Reseller</li><li>Ongoing Consultation</li><li>Consulting Services for World</li><li>Software Integration</li></ul>
  <div class="more">Read <span>More</span></div>
</article>
<aside class="abs contact">
  <h2>Quick <span>Contact</span></h2>
  <div class="field">Name:</div><div class="field">Company:</div><div class="field">E-mail:</div><div class="field">Phone:</div>
  <div class="field">Areas of Interest:<svg width="10" height="10"><rect width="10" height="10" fill="#ddd" stroke="#888"/><path d="M2 3h6L5 7z" fill="#333"/></svg></div>
  <div class="field tall">Comments:</div>
  <div class="actions">
    <div class="btn">Submit<i><svg width="12" height="10"><path d="M1 5l3.5 3.5L11 1" stroke="#fff" stroke-width="2" fill="none"/></svg></i></div>
    <div class="btn ghost">Clear<i><svg width="12" height="10"><path d="M1 5l3.5 3.5L11 1" stroke="#fff" stroke-width="2" fill="none"/></svg></i></div>
  </div>
</aside>

<div class="abs partners"><span>Corvane</span><span>Helvix</span><span>Ibrant</span><span>Sentrix</span><span>Delmor</span><span>Gravio</span></div>
<div class="abs pager" style="left:246px"><svg width="8" height="10"><path d="M6 1L2 5l4 4" stroke="#fff" stroke-width="2" fill="none"/></svg></div>
<div class="abs pager" style="left:927px"><svg width="8" height="10"><path d="M2 1l4 4-4 4" stroke="#fff" stroke-width="2" fill="none"/></svg></div>

<footer class="abs footer">
  <h3 style="left:242px;top:28px">Quick Links</h3>
  <ul class="links" style="left:244px;top:50px"><li>Company</li><li>Products</li><li>LEDGRA</li><li>Services</li><li>Clientele</li></ul>
  <ul class="links" style="left:354px;top:50px"><li>Careers</li><li>Infobin</li><li>Enquiry</li><li>Sitemap</li><li>Contact</li></ul>
  <div class="vrule" style="left:465px"></div>
  <h3 style="left:493px;top:28px">Support Center</h3>
  <ul class="links wide" style="left:494px;top:50px"><li>Free Assessment</li><li>Client Portal Login</li><li>Laecieas Deugtrat</li><li>Maecieas feiogtrat</li><li>Free Assessment</li></ul>
  <div class="vrule" style="left:621px"></div>
  <h3 style="left:642px;top:27px">Connect with Us</h3>
  <div class="social" style="left:644px;top:56px">Netlinker<i></i></div>
  <div class="social" style="left:644px;top:101px">Peoplebook<i></i></div>
  <div class="vrule" style="left:755px"></div>
  <div class="f-brand"><span style="width:12px;height:12px;background:#b87a2c;border-radius:50%"></span><div>QUANTREL<br>INFORMATION<br>SYSTEMS PTE LTD</div></div>
  <div class="subscribe">Subscribe with Us</div>
  <div class="sub-row"><div>email address</div><div>Subscribe</div></div>
</footer>
<div class="abs copyright">© Copyrights 2013. Quantrel Information Systems. All Rights Reserved.</div>
</body>
</html>
```